DORLIT HOMES Professional Home Buyers

Please see two files uploaded. One is my new LOGO (thanks Quenby) and the other gives the wording and pages desired. Of course I am open to suggestions to further enhance what I'm about. I don't want testimonials or houses to buy to appear but to have room for them when I'm ready. I am a real estate investor not a licensed real estate agent. For FAQ i want just the questions to appear and when they click on the question the answer appears and when they click on the question again the answer disappears. make sense? When you read my wording and my idea of pages you'll get an idea of what I'm about. Suggestions are welcomed.

Industry/Entity Type

Real Estate

Number of Pages Required

5+ page

Requirements
Must have
• FAQ pages only questions appear. They click on question the answer appears underneath. they click on question again, the answer disappears. Also, I of course, want my new LOGO to appear on each page I don't know if it will look better all by itself or blended in somehow? Call now 418-555-0193 on each page also. I will get a real phone number before website goes live. If you have a better way of wording what I'm describing please let me know, I am open to feedback
Nice to have
• Anything that the average homeowner can relate to (yea I know, that doesn't help you much, right?)
• Testimonial page and houses to buy page could be done with just the shell ready in the wings for when my business grows it will be ready all that it would need then are the wording and pictures to be uploaded onto the website page. make sense?
Should not have
• I don't want it too elegant or rich looking as I believe my audience will be mostly the average homeowner who needs help

```html
<!DOCTYPE html>
<html lang="en">
<head>
<meta charset="utf-8">
<title>DORLIT HOMES – Professional Home Buyers</title>
<link rel="stylesheet" href="https://fonts.googleapis.com/css2?family=Montserrat:wght@400;600;700;800&family=Raleway:wght@200;300;400;600;800;900&display=swap">
<style>
  :root{
    --navy:#232d45;
    --navy-deep:#161d30;
    --blue:#2f7fd0;
    --heading-blue:#2b5fa6;
    --text:#6b6f78;
    --slate:#7c859c;
    --slate-box:#4c566f;
    --orange:#f5a623;
    --pill:#eeeff2;
    --footer:#2a2b2e;
    --white:#ffffff;
  }
  *{box-sizing:border-box;margin:0;padding:0}
  html,body{width:1200px;height:2436px;overflow:hidden}
  body{font-family:"Raleway",sans-serif;color:var(--text);background:var(--white)}
  .page{width:1200px;height:2436px;position:relative}

  /* Hero */
  .hero{position:relative;height:760px;color:var(--white);text-align:center;overflow:hidden}
  .hero-photo{position:absolute;inset:0;background:
      linear-gradient(180deg,rgba(22,29,48,.55),rgba(22,29,48,.85)),
      linear-gradient(115deg,#3b4663 0%,#222b42 40%,#4a5877 62%,#1c2336 100%)}
  .nav{position:relative;display:flex;align-items:center;justify-content:center;gap:30px;padding-top:46px;font-family:"Montserrat",sans-serif;font-size:15px;font-weight:600;letter-spacing:1px}
  .nav a{color:var(--white);text-decoration:none}
  .nav .phone{margin-left:40px;border:2px solid var(--white);padding:10px 18px;font-size:16px}
  .brand-badge{position:relative;margin:56px auto 0;width:240px;height:200px;background:var(--white);border-radius:14px;display:flex;align-items:center;justify-content:center;gap:10px;color:var(--navy);font-family:"Montserrat",sans-serif;font-weight:800;font-size:24px;letter-spacing:1px}
  .brand-badge .mark{width:18px;height:18px;background:var(--navy)}
  .hero h1{position:relative;margin-top:56px;font-family:"Montserrat",sans-serif;font-weight:800;font-size:62px;letter-spacing:6px}
  .hero .tag{position:relative;font-family:"Montserrat",sans-serif;font-weight:400;font-size:22px;letter-spacing:8px;color:rgba(255,255,255,.55);margin-top:2px}
  .hero .tag-strong{position:relative;font-family:"Montserrat",sans-serif;font-weight:700;font-size:28px;letter-spacing:4px;margin-top:4px}
  .btn-solid{position:relative;display:inline-block;margin-top:22px;background:var(--blue);color:var(--white);font-family:"Montserrat",sans-serif;font-size:15px;font-weight:600;letter-spacing:2px;padding:18px 40px;border-radius:3px}

  /* Intro */
  .intro{height:400px;text-align:center;padding-top:68px}
  .section-title{font-family:"Montserrat",sans-serif;font-weight:700;font-size:24px;letter-spacing:1px;color:var(--heading-blue)}
  .divider{width:3px;height:14px;background:var(--heading-blue);margin:12px auto 28px}
  .intro p{width:720px;margin:0 auto;font-size:15px;line-height:26px}
  .btn-outline{display:inline-flex;align-items:center;gap:14px;border:2px solid #8a8e97;color:#4b4f58;font-family:"Montserrat",sans-serif;font-size:15px;font-weight:600;letter-spacing:3px;padding:16px 40px;border-radius:3px}
  .btn-outline svg{width:16px;height:16px}
  .intro .btn-outline{margin-top:40px}

  /* Cash */
  .cash{height:660px;background:var(--slate);text-align:center;padding-top:80px;color:var(--white)}
  .cash-box{width:440px;height:300px;margin:0 auto;background:var(--slate-box);border:2px solid rgba(255,255,255,.25);display:flex;flex-direction:column;justify-content:center;align-items:center}
  .cash-box .light{font-weight:200;font-size:62px;letter-spacing:4px;line-height:1}
  .cash-box .mid{font-weight:300;font-size:26px;letter-spacing:8px;margin-top:10px}
  .cash-box .heavy{font-weight:900;font-size:84px;letter-spacing:2px;line-height:1;margin-top:6px}
  .cash p{width:740px;margin:44px auto 0;font-size:15px;line-height:26px;color:rgba(255,255,255,.9)}
  .cash .btn-outline{margin-top:40px;border-color:var(--white);color:var(--white)}

  /* Sell */
  .sell{height:400px;text-align:center;padding-top:100px}
  .sell .section-title{display:inline-flex;align-items:center;gap:10px}
  .sell .fast{background:var(--orange);color:var(--white);padding:4px 10px;border-radius:4px}
  .pills{display:flex;flex-wrap:wrap;justify-content:center;gap:22px 36px;width:1100px;margin:48px auto 0}
  .pill{background:var(--pill);font-family:"Montserrat",sans-serif;font-size:13px;font-weight:600;letter-spacing:1px;color:#555a63;padding:18px 34px;border-radius:3px}

  /* Footer */
  .footer{height:216px;background:var(--footer);color:#9a9ca2;padding:82px 110px 0;display:flex;justify-content:space-between}
  .footer nav{display:flex;gap:34px;font-family:"Montserrat",sans-serif;font-size:13px;font-weight:600;letter-spacing:1px}
  .footer .copy{margin-top:20px;font-size:13px}
  .footer .copy b{color:var(--white)}
  .social{display:flex;gap:8px;margin-top:14px}
  .social span{width:46px;height:46px;display:block}
  .s1{background:#3b5998}.s2{background:#1da1f2}.s3{background:#dd4b39}.s4{background:#0077b5}
</style>
</head>
<body>
<div class="page">
  <header class="hero">
    <div class="hero-photo" role="img" aria-label="Photo looking up at tall city office towers in dark blue tones"></div>
    <nav class="nav">
      <a>HOME</a><a>ABOUT US</a><a>FAQ</a><a>CONTACT US</a><a>TESTIMONIALS</a><a>HOUSES TO BUY</a>
      <span class="phone">418-555-0193</span>
    </nav>
    <div class="brand-badge"><span class="mark"></span>DORLIT HOMES</div>
    <h1>DORLIT HOMES</h1>
    <div class="tag">WILL BUY YOUR HOUSE AS IS</div>
    <div class="tag-strong">FAST AND HASSLE</div>
    <a class="btn-solid">LEARN MORE</a>
  </header>

  <section class="intro">
    <h2 class="section-title">WE BUY HOUSES IN ANY CONDITION!</h2>
    <div class="divider"></div>
    <p>Don't waste another penny on expensive repairs! DORLIT HOMES is currently buying houses throughout Calverton County. We buy houses "as is", so you can sell fast, we handle all traditional closing costs and we can close in as quickly as a week. Contact us today for your free, no obligation quote.</p>
    <a class="btn-outline"><svg viewBox="0 0 16 16"><path d="M3 8h10M9 4l4 4-4 4" fill="none" stroke="currentColor" stroke-width="2"/></svg>GET YOUR FREE QUOTE</a>
  </section>

  <section class="cash">
    <div class="cash-box">
      <div class="light">GET CASH</div>
      <div class="mid">FOR YOUR</div>
      <div class="heavy">HOUSE!</div>
    </div>
    <p>DORLIT HOMES has real estate investors ready to buy your house in as little as seven days. We buy houses, townhouses, condos, duplexes and multi-family buildings from owners looking to sell quickly.</p>
    <a class="btn-outline"><svg viewBox="0 0 16 16"><path d="M3 8h10M9 4l4 4-4 4" fill="none" stroke="currentColor" stroke-width="2"/></svg>GET MORE INFO</a>
  </section>

  <section class="sell">
    <h2 class="section-title">SELL YOUR HOME <span class="fast">FAST!</span></h2>
    <div class="pills">
      <span class="pill">WE PAY ALL CASH</span>
      <span class="pill">WE PAY MOST CLOSING COSTS</span>
      <span class="pill">WE BUY "AS IS"</span>
      <span class="pill">NO WAITING FOR BANK LOAN APPROVALS</span>
      <span class="pill">QUICK CLOSINGS</span>
    </div>
  </section>

  <footer class="footer">
    <div>
      <nav><span>HOME</span><span>ABOUT US</span><span>FAQ</span><span>CONTACT US</span><span>TESTIMONIALS</span><span>HOUSES TO BUY</span></nav>
      <div class="copy">© 2016 <b>DORLIT HOMES</b> · All Rights Reserved</div>
    </div>
    <div class="social"><span class="s1"></span><span class="s2"></span><span class="s3"></span><span class="s4"></span></div>
  </footer>
</div>
</body>
</html>
```